Brimvane.com fiber optic internet website redesign

We need a new website design for our fiber optic internet company that provides internet, phone, and tv services. It should use the text "Marrowfen fiber optics", and "I beamed up with Marrowfen". The design should use the color blue and the attached logo.
We are a 30 year old internet company who started as a dial up internet provider in our basement. Today we design, build, and maintain our own fiber optic internet network to provide service to residential, business, educational, healthcare, and governmental customers

```html
<!DOCTYPE html>
<html lang="en">
<head>
<meta charset="utf-8">
<title>Marrowfen Fiber Optics</title>
<link href="https://fonts.googleapis.com/css2?family=Poppins:wght@400;500;600;700;800&display=swap" rel="stylesheet">
<style>
:root{
  --blue:#0a4f98;
  --blue-deep:#06458a;
  --teal:#80bfcb;
  --grey-card:#d9d9d9;
  --ink:#111;
  --footer:#060b18;
  --white:#fff;
  --sky:#3bb0e8;
}
*{margin:0;padding:0;box-sizing:border-box}
html,body{width:1200px;height:2965px;overflow:hidden;background:var(--white)}
body{position:relative;font-family:'Poppins',sans-serif;color:var(--ink)}
.abs{position:absolute}
/* header */
.brand{left:155px;top:8px;display:flex;align-items:center;gap:10px}
.brand-dot{width:40px;height:40px;border-radius:50%;background:var(--blue)}
.brand-name{font-size:22px;font-weight:700;color:var(--blue)}
.nav a{position:absolute;top:43px;font-size:11px;font-weight:600;color:var(--ink);text-decoration:none;letter-spacing:.2px}
.btn{display:flex;align-items:center;justify-content:center;font-size:11px;font-weight:700;text-decoration:none;border-radius:3px}
.btn-blue{background:var(--blue);color:var(--white)}
/* hero */
.hero{left:0;top:99px;width:1200px;height:653px;overflow:hidden}
.hero-title{left:151px;font-size:60px;font-weight:800;color:transparent;-webkit-text-stroke:2px var(--white);line-height:1;letter-spacing:-1px}
.hero-copy{left:151px;top:435px;width:460px;font-size:10.4px;line-height:15px;color:var(--white)}
.btn-white{background:var(--white);color:var(--ink)}
.btn-black{background:#000;color:var(--white)}
/* services */
.section-title{font-size:42px;font-weight:800;color:var(--white);-webkit-text-stroke:2px var(--ink);letter-spacing:-1px;line-height:1}
.services{left:150px;top:938px;width:899px;height:293px;display:flex}
.service{flex:1;text-align:center;padding-top:8px}
.service h3{font-size:17px;font-weight:600;margin-top:34px}
.service p{font-size:11.6px;line-height:17px;margin:20px 8px 0}
.s-internet{background:var(--grey-card);border-top-left-radius:18px}
.s-phone{background:var(--teal)}
.s-tv{background:var(--blue);border-bottom-right-radius:18px;color:#111}
.s-tv p{color:#0d2b50}
/* packages */
.pkg-eyebrow{left:0;width:1200px;top:1490px;text-align:center;font-size:18px;font-weight:500}
.pkg-heading{left:0;width:1200px;top:1520px;text-align:center;font-size:23px;font-weight:600;color:var(--blue)}
.pkg{top:1588px;width:263px;height:370px;border:2px solid var(--teal);border-radius:8px;overflow:hidden;text-align:center;background:var(--white)}
.pkg-head{height:111px;background:var(--teal);display:flex;align-items:center;justify-content:center}
.pkg-head h4{font-size:15.5px;font-weight:800;color:var(--teal);-webkit-text-stroke:1.2px #111;letter-spacing:-.3px}
.pkg ul{list-style:none;margin-top:41px;font-size:8.6px;font-weight:500;line-height:23.5px}
.price{margin-top:10px;font-size:16px;font-weight:500}
.price b{color:var(--blue);font-weight:700}
.pkg .btn{width:109px;height:25px;margin:54px auto 0}
/* about */
.about-copy{left:151px;top:2207px;width:335px;font-size:10.4px;line-height:15px}
/* footer */
.footer{left:0;top:2471px;width:1200px;height:494px;background:var(--footer);color:var(--white)}
.f-h{position:absolute;font-size:13px;font-weight:600}
.f-row{position:absolute;display:flex;gap:10px;font-size:11.5px;line-height:17px;color:#e8e8e8}
.f-row svg{flex:none;margin-top:1px}
.f-link{position:absolute;left:563px;font-size:12.5px;color:#e8e8e8}
.f-input{position:absolute;left:793px;top:174px;width:169px;height:29px;border:1px solid #2f7fd0;font-size:13px;padding:5px 5px;color:#e8e8e8}
.f-rule{position:absolute;left:148px;top:408px;width:899px;height:1px;background:#888}
.f-social{position:absolute;top:443px;width:16px;height:16px;border-radius:50%;background:var(--white)}
</style>
</head>
<body>

<header>
  <div class="abs brand"><span class="brand-dot"></span><span class="brand-name">Marrowfen</span></div>
  <nav class="nav">
    <a style="left:404px" href="#">HOME</a>
    <a style="left:467px" href="#">SERVICES</a>
    <a style="left:549px" href="#">PACKAGES</a>
    <a style="left:639px" href="#">ABOUT US</a>
    <a style="left:724px" href="#">CONTACT US</a>
  </nav>
  <a class="abs btn btn-blue" style="left:917px;top:37px;width:108px;height:25px" href="#">GET CONNECTED</a>
</header>

<section class="abs hero">
  <svg width="1200" height="653" role="img" aria-label="Photo of a team reviewing documents together at an office desk">
    <defs>
      <linearGradient id="heroPhoto" x1="0" y1="0" x2="1" y2="1">
        <stop offset="0" stop-color="#6b6f74"/>
        <stop offset=".5" stop-color="#4a4e55"/>
        <stop offset="1" stop-color="#9a9c9e"/>
      </linearGradient>
    </defs>
    <rect width="1200" height="653" fill="url(#heroPhoto)"/>
    <polygon points="0,0 250,0 725,653 0,653" fill="#3a78b8" opacity=".85"/>
  </svg>
</section>
<div class="abs hero-title" style="top:276px">MARROWFEN</div>
<div class="abs hero-title" style="top:360px">FIBER OPTICS</div>
<p class="abs hero-copy">For over 30 years, Marrowfen Fiber Optics has been delivering reliable internet, phone, and TV services to residential, business, educational, healthcare, and governmental customers. Starting as a dial-up internet provider in a basement, we've grown into a trusted leader in fiber optic technology, designing, building, and maintaining our own network. With a commitment to innovation and customer satisfaction, we proudly declare, "I beamed up with Marrowfen," as we continue to connect communities with cutting-edge solutions and unmatched reliability.</p>
<a class="abs btn btn-white" style="left:151px;top:566px;width:109px;height:25px" href="#">GET CONNECTED</a>
<a class="abs btn btn-black" style="left:278px;top:566px;width:109px;height:25px" href="#">VIEW PACKAGES</a>

<h2 class="abs section-title" style="left:0;width:1200px;text-align:center;top:842px">SERVICES</h2>

<section class="abs services">
  <article class="service s-internet">
    <svg width="72" height="72" viewBox="0 0 72 72"><path d="M4 30 A46 46 0 0 1 68 30 L62 37 A37 37 0 0 0 10 37Z M15 41 A30 30 0 0 1 57 41 L51 48 A21 21 0 0 0 21 48Z M26 52 A14 14 0 0 1 46 52 L36 64Z" fill="#000"/></svg>
    <h3>INTERNET SERVICES</h3>
    <p>Lorem ipsum dolor sit amet, consectetur adipiscing elit. Sed ut quam mauris. Cras posuere, erat non gravida eleifend, urna erat sagittis nisi, et ultrices nulla augue et odio. Aliquam dapibus molestie urna.</p>
  </article>
  <article class="service s-phone">
    <svg width="80" height="74" viewBox="0 0 80 74"><rect x="13" y="2" width="38" height="70" rx="5" fill="#000"/><rect x="17" y="10" width="30" height="50" fill="var(--teal)"/><circle cx="32" cy="66" r="3" fill="var(--teal)"/><path d="M56 28 q5 9 0 18 M62 22 q9 15 0 30 M68 16 q13 21 0 42" stroke="#000" stroke-width="2.5" fill="none"/></svg>
    <h3>PHONE SERVICES</h3>
    <p>Lorem ipsum dolor sit amet, consectetur adipiscing elit. Sed ut quam mauris. Cras posuere, erat non gravida eleifend, urna erat sagittis nisi, et ultrices nulla augue et odio. Aliquam dapibus molestie urna.</p>
  </article>
  <article class="service s-tv">
    <svg width="74" height="74" viewBox="0 0 74 74"><path d="M27 4 L37 24 L47 4" stroke="#000" stroke-width="3" fill="none"/><rect x="4" y="24" width="66" height="44" rx="3" fill="#000"/><rect x="10" y="30" width="40" height="32" fill="var(--blue)"/><circle cx="60" cy="38" r="3" fill="var(--blue)"/><circle cx="60" cy="50" r="3" fill="var(--blue)"/><rect x="14" y="68" width="8" height="5" fill="#000"/><rect x="52" y="68" width="8" height="5" fill="#000"/></svg>
    <h3>TV SERVICES</h3>
    <p>Lorem ipsum dolor sit amet, consectetur adipiscing elit. Sed ut quam mauris. Cras posuere, erat non gravida eleifend, urna erat sagittis nisi, et ultrices nulla augue et odio. Aliquam dapibus molestie urna.</p>
  </article>
</section>

<svg class="abs" style="left:0;top:1313px" width="1200" height="290" role="img" aria-label="Decorative band of blue light shards fading into white">
  <defs>
    <linearGradient id="shardFade" x1="0" y1="0" x2="0" y2="1">
      <stop offset="0" stop-color="#2aa6e6"/>
      <stop offset=".45" stop-color="#7cc8f0" stop-opacity=".7"/>
      <stop offset="1" stop-color="#ffffff" stop-opacity="0"/>
    </linearGradient>
  </defs>
  <rect width="1200" height="290" fill="url(#shardFade)"/>
</svg>

<div class="abs pkg-eyebrow">PACKAGES</div>
<div class="abs pkg-heading">MARROWFEN FIBER OPTICS SERVICE PACKAGES</div>

<article class="abs pkg" style="left:182px">
  <div class="pkg-head"><h4>RESIDENTIAL PACKAGES</h4></div>
  <ul><li>HIGH-SPEED INTERNET (200 MBPS)</li><li>UNLIMITED LOCAL AND LONG-DISTANCE PHONE</li><li>ESSENTIAL TV CHANNELS WITH HD STREAMING</li></ul>
  <div class="price"><b>$20.00</b> / MONTH</div>
  <a class="btn btn-blue" href="#">READ MORE</a>
</article>
<article class="abs pkg" style="left:468px">
  <div class="pkg-head"><h4>BUSINESS PACKAGES</h4></div>
  <ul><li>INTERNET UP TO 500 MBPS</li><li>BUSINESS PHONE LINE WITH CALL MANAGEMENT FEATURES</li><li>OPTIONAL TV FOR WAITING AREAS OR OFFICE LOUNGES</li></ul>
  <div class="price"><b>$30.00</b> / MONTH</div>
  <a class="btn btn-blue" href="#">READ MORE</a>
</article>
<article class="abs pkg" style="left:754px">
  <div class="pkg-head"><h4>EDUCATION PACKAGES</h4></div>
  <ul><li>SCALABLE INTERNET SPEEDS FOR CLASSROOMS AND DORMS</li><li>RELIABLE PHONE LINES FOR ADMINISTRATION AND STAFF</li><li>OPTIONAL EDUCATIONAL PROGRAMMING VIA TV</li></ul>
  <div class="price"><b>$40.00</b> / MONTH</div>
  <a class="btn btn-blue" href="#">READ MORE</a>
</article>

<h2 class="abs section-title" style="left:151px;top:2148px;font-size:38px">ABOUT US</h2>
<p class="abs about-copy">Lorem ipsum dolor sit amet, consectetur adipiscing elit. Sed ut quam mauris. Cras posuere, erat non gravida eleifend, urna erat sagittis nisi, et ultrices nulla augue et odio. Aliquam dapibus molestie urna. Integer ac diam pharetra nibh gravida facilisis. Sed at ligula in nisi maximus cursus sed quis ipsum. Sed purus mi, accumsan eget placerat volutpat, rutrum quis arcu.</p>
<svg class="abs" style="left:545px;top:2048px" width="502" height="334" role="img" aria-label="Photo of a man working on a laptop by an office window">
  <defs>
    <linearGradient id="aboutPhoto" x1="0" y1="0" x2="1" y2="0">
      <stop offset="0" stop-color="#3a5f7e"/>
      <stop offset=".6" stop-color="#5a6a78"/>
      <stop offset="1" stop-color="#2a2f3a"/>
    </linearGradient>
  </defs>
  <rect width="502" height="334" fill="url(#aboutPhoto)"/>
  <polygon points="0,0 120,0 370,334 0,334" fill="#2f6aa8" opacity=".6"/>
</svg>

<footer class="abs footer">
  <div class="f-h" style="left:237px;top:127px">Contact Information</div>
  <div class="f-row" style="left:237px;top:177px">
    <svg width="13" height="16" viewBox="0 0 13 16"><path d="M6.5 1 A5 5 0 0 1 11.5 6 C11.5 10 6.5 15 6.5 15 C6.5 15 1.5 10 1.5 6 A5 5 0 0 1 6.5 1Z" fill="none" stroke="#fff" stroke-width="1.4"/><circle cx="6.5" cy="6" r="1.8" fill="#fff"/></svg>
    <span>48 Alder Lane<br>Fernbrook<br>USA</span>
  </div>
  <div class="f-row" style="left:237px;top:233px">
    <svg width="14" height="14" viewBox="0 0 14 14"><circle cx="7" cy="7" r="6" fill="none" stroke="#fff" stroke-width="1.2"/><ellipse cx="7" cy="7" rx="2.6" ry="6" fill="none" stroke="#fff" stroke-width="1"/><path d="M1 7 H13" stroke="#fff"/></svg>
    <span>marrowfen-fiber.net</span>
  </div>
  <div class="f-row" style="left:237px;top:262px">
    <svg width="14" height="14" viewBox="0 0 14 14"><rect x="1" y="3" width="12" height="9" fill="none" stroke="#fff" stroke-width="1.2"/><path d="M1 3 L7 8 L13 3" fill="none" stroke="#fff" stroke-width="1.2"/></svg>
    <span>hello@marrowfen-fiber.net</span>
  </div>
  <div class="f-row" style="left:237px;top:290px">
    <svg width="14" height="16" viewBox="0 0 14 16"><rect x="3" y="1" width="8" height="14" rx="1" fill="none" stroke="#fff" stroke-width="1.2"/><path d="M6 12.5 H8" stroke="#fff"/></svg>
    <span>1-888-555-0142</span>
  </div>

  <div class="f-h" style="left:563px;top:127px">Quick Links</div>
  <div class="f-link" style="top:174px">HOME</div>
  <div class="f-link" style="top:205px">SERVICES</div>
  <div class="f-link" style="top:237px">PACKGAES</div>
  <div class="f-link" style="top:268px">ABOUT</div>
  <div class="f-link" style="top:299px">CONTACT</div>

  <div class="f-h" style="left:793px;top:130px">Contact Us</div>
  <div class="f-input">Email</div>

  <div class="f-rule"></div>
  <span class="f-social" style="left:842px"></span>
  <span class="f-social" style="left:884px"></span>
  <span class="f-social" style="left:925px"></span>
  <span class="f-social" style="left:966px"></span>
  <span class="f-social" style="left:1007px"></span>
</footer>

</body>
</html>
```